Flyer Design Project

Need a DL Size flyer (2 sided) for letter box marketing for our website www.brightwardsecure.com.au

Project Deadline Extended
Reason: Thank you for submitting the designs. We like few of the designs and will request those designers to changes few things to make it more suitable for us. Because of holidays need to extend the deadlines. Thank you.

Industry/Entity Type

Marketing

```html
<!DOCTYPE html>
<html lang="en">
<head>
<meta charset="utf-8">
<title>Brightward Secure – CCTV Packages Flyer</title>
<link rel="stylesheet" href="https://fonts.googleapis.com/css2?family=Roboto:wght@400;500;700;900&family=Arimo:wght@400;700&display=swap">
<style>
  :root {
    --navy: #1b2a63;
    --navy-deep: #142052;
    --blue: #1f5fb0;
    --blue-light: #3b8ee0;
    --yellow: #f7c21a;
    --yellow-soft: #f9cf3a;
    --white: #ffffff;
    --ink: #1e1e1e;
    --grey-band: #d9dbe0;
    --grey-text: #555a66;
    --photo-fill: #e6e8ec;
  }
  * { box-sizing: border-box; margin: 0; padding: 0; }
  html, body { width: 1170px; height: 1200px; overflow: hidden; background: var(--white); }
  body { position: relative; font-family: "Roboto", Arial, sans-serif; color: var(--ink); }

  .hero {
    position: absolute; left: 32px; top: 4px; width: 1106px; height: 578px;
    background:
      linear-gradient(115deg, rgba(10,25,80,0.55) 0%, rgba(10,25,80,0) 38%),
      linear-gradient(160deg, rgba(255,255,255,0) 55%, rgba(12,30,95,0.55) 56%, rgba(12,30,95,0.55) 70%, rgba(255,255,255,0) 71%),
      radial-gradient(ellipse at 70% 45%, var(--blue-light) 0%, var(--blue) 45%, var(--navy) 100%);
    overflow: hidden;
  }
  .brand-name {
    position: absolute; left: 57px; top: 52px;
    font-family: "Arimo", Arial, sans-serif; font-weight: 700; font-size: 48px;
    color: var(--yellow); letter-spacing: 0.5px; line-height: 1;
  }
  .brand-tagline {
    position: absolute; left: 57px; top: 104px;
    font-family: "Arimo", Arial, sans-serif; font-weight: 700; font-size: 24px;
    color: var(--white); letter-spacing: 1px;
  }
  .brand-contact {
    position: absolute; left: 57px; top: 150px;
    font-size: 11px; font-weight: 700; color: var(--white); line-height: 1.35;
  }
  .services {
    position: absolute; left: 753px; top: 80px;
    font-family: "Arimo", Arial, sans-serif; font-weight: 700; font-size: 25px;
    color: var(--white); line-height: 1.2;
  }
  .intro {
    position: absolute; left: 57px; top: 268px; width: 480px;
    font-size: 20px; color: var(--white); line-height: 1.3;
  }
  .promises {
    position: absolute; left: 57px; top: 436px;
    font-family: "Arimo", Arial, sans-serif; font-weight: 700; font-size: 24px;
    color: var(--white); line-height: 1.33;
    list-style: none;
  }
  .hero-visual {
    position: absolute; left: 560px; top: 244px; width: 530px; height: 334px;
    background: linear-gradient(100deg, #1c2230 0%, #4a4036 45%, #8d6f52 75%, #c9a27c 100%);
  }

  .packages {
    position: absolute; left: 32px; top: 599px; width: 1106px; height: 566px;
    background: linear-gradient(180deg, var(--yellow-soft), var(--yellow));
  }
  .package { position: absolute; width: 340px; text-align: center; }
  .package-shot {
    position: relative; height: 136px; background: var(--white);
  }
  .package-photo {
    position: absolute; left: 12px; top: 30px; right: 12px; bottom: 4px;
    background: var(--photo-fill);
  }
  .price-tag {
    position: absolute; left: 10px; top: -4px; z-index: 1;
    background: var(--navy); color: var(--white);
    font-weight: 700; font-size: 19px; padding: 4px 12px 5px;
  }
  .price-tag sup { font-size: 9px; vertical-align: 8px; }
  .package-head {
    background: linear-gradient(180deg, #f2f3f5, var(--grey-band));
    padding: 6px 0 4px;
  }
  .package-title { font-size: 24px; font-weight: 500; color: var(--ink); line-height: 1.1; }
  .package-kind { font-size: 11px; color: var(--grey-text); }
  .package-spec {
    margin-top: 6px; font-size: 9.5px; line-height: 1.3; color: var(--ink); padding: 0 4px;
  }
  .col-1 { left: 36px; } .col-2 { left: 383px; } .col-3 { left: 730px; }
  .row-1 { top: 21px; } .row-2 { top: 264px; }

  .footer-bar {
    position: absolute; left: 0; bottom: 0; width: 100%; height: 50px;
    background: var(--navy-deep); color: var(--white);
    font-size: 17px; font-weight: 500;
    display: flex; align-items: center; justify-content: center;
  }
</style>
</head>
<body>
  <header class="hero">
    <h1 class="brand-name">Brightward Secure</h1>
    <p class="brand-tagline">CCTV System Specialist</p>
    <p class="brand-contact">14/6 Larkin Street, Riverton, NSW 2199<br>02 9040 3318 | info@brightwardsecure.com.au<br>www.brightwardsecure.com.au</p>
    <p class="services">Security Alarms and<br>CCTV Camera Providers</p>
    <p class="intro">Brightward Secure<br>is dedicated to providing high quality CCTV System at affordable prices.<br>All of our packages include hardware, software, accessories and full installation.</p>
    <ul class="promises">
      <li>High quality hardware</li>
      <li>100% customer satisfaction</li>
      <li>1 year full warranty</li>
      <li>14 days money back guarantee</li>
    </ul>
    <div class="hero-visual" role="img" aria-label="Photo of a monitor showing a multi-camera CCTV view, beside a hand holding a smartphone with the CCTV app"></div>
  </header>

  <section class="packages">
    <article class="package col-1 row-1">
      <div class="package-shot"><span class="price-tag">$1495<sup>+GST*</sup></span><div class="package-photo" role="img" aria-label="Photo of two dome cameras, DVR recorder and LCD monitor"></div></div>
      <div class="package-head"><h2 class="package-title">Package 1</h2><p class="package-kind">Standalone DVR System (2 Cameras)</p></div>
      <p class="package-spec">2 X high resolution dome cameras, 1 X 4 channel standalone DVR 500GB hard drive, 19" LCD monitor, Remote access from PCs &amp; Phones*<br>Easy to use, 1 Year Warranty, Full system supplied &amp; installed</p>
    </article>
    <article class="package col-2 row-1">
      <div class="package-shot"><span class="price-tag">$2195<sup>+GST*</sup></span><div class="package-photo" role="img" aria-label="Photo of four dome cameras, DVR recorder and LCD monitor"></div></div>
      <div class="package-head"><h2 class="package-title">Package 2</h2><p class="package-kind">Standalone DVR System (4 Cameras)</p></div>
      <p class="package-spec">4 X high resolution dome cameras, 1 X 4 channel standalone DVR 500GB hard drive, 19" LCD monitor, Remote access from PCs &amp; Phones*<br>Easy to use, 1 Year Warranty, Full system supplied &amp; installed</p>
    </article>
    <article class="package col-3 row-1">
      <div class="package-shot"><span class="price-tag">$3295<sup>+GST*</sup></span><div class="package-photo" role="img" aria-label="Photo of eight dome cameras, DVR recorder and LCD monitor"></div></div>
      <div class="package-head"><h2 class="package-title">Package 3</h2><p class="package-kind">Standalone DVR System (8 Cameras)</p></div>
      <p class="package-spec">8 X high resolution dome cameras, 1 X 8 channel standalone DVR 1 Terabyte hard drive, 19" LCD monitor, Remote access from PCs &amp; Phones*<br>Easy to use, 1 Year Warranty, Full system supplied &amp; installed</p>
    </article>
    <article class="package col-1 row-2">
      <div class="package-shot"><span class="price-tag">$1995<sup>+GST*</sup></span><div class="package-photo" role="img" aria-label="Photo of two IP cameras, PC based NVR and LCD monitor"></div></div>
      <div class="package-head"><h2 class="package-title">Package 4</h2><p class="package-kind">IP based CCTV System (2 Cameras)</p></div>
      <p class="package-spec">2 X 2 Megapixel IP Cameras, 1 X PC based NVR System, 500GB hard drive 19" LCD Monitor, Remote Access from PCs and Phones*<br>Easy to use, 1 Year warranty, Full system supplied &amp; installed</p>
    </article>
    <article class="package col-2 row-2">
      <div class="package-shot"><span class="price-tag">$3295<sup>+GST*</sup></span><div class="package-photo" role="img" aria-label="Photo of four IP cameras, PC based NVR and LCD monitor"></div></div>
      <div class="package-head"><h2 class="package-title">Package 5</h2><p class="package-kind">IP based CCTV System (4 Cameras)</p></div>
      <p class="package-spec">4 X 2 Megapixel IP Cameras, 1 X PC based NVR System, 1 Terabyte hard drive 19" LCD Monitor, Remote Access from PCs and Phones*<br>Easy to use, 1 Year warranty, Full system supplied &amp; installed</p>
    </article>
    <article class="package col-3 row-2">
      <div class="package-shot"><span class="price-tag">$4495<sup>+GST*</sup></span><div class="package-photo" role="img" aria-label="Photo of eight IP cameras, PC based NVR and LCD monitor"></div></div>
      <div class="package-head"><h2 class="package-title">Package 6</h2><p class="package-kind">IP based CCTV System (8 Cameras)</p></div>
      <p class="package-spec">8 X 2 Megapixel IP Cameras, 1 X PC based NVR System, 2 Terabyte hard drive 19" LCD Monitor, Remote Access from PCs and Phones*<br>Easy to use, 1 Year warranty, Full system supplied &amp; installed</p>
    </article>
    <footer class="footer-bar">14/6 Larkin Street, Riverton, NSW 2199 | 02 9040 3318 | info@brightwardsecure.com.au | www.brightwardsecure.com.au</footer>
  </section>
</body>
</html>
```